Skin care manufacturer looking for packaging design for new skin care brand.

We need a design and logo for a skin care brand to be sold at retail stores and online in the United States and Europe. The design will be for 1.7oz - 2oz serums that will not have a retail box. The name of the brand is Velora Fen and should be a luxurious brand that is approachable. The brand will consist of 4 face serums - Vitamin C, Collagen, Retinol and Hyaluronic Acid that all contain Dead Sea Minerals. Images shown are for inspiration only. Color of bottles can be varied based on design and bottles can be screen printed or labeled.

```html
<!DOCTYPE html>
<html lang="en">
<head>
<meta charset="utf-8">
<title>Velora Fen Serum Labels</title>
<link rel="stylesheet" href="https://fonts.googleapis.com/css2?family=Montserrat:wght@300;400;500&display=swap">
<style>
  :root {
    --canvas-bg: #e3e3e3;
    --label-white: #f4f4f4;
    --label-sheen: #e9e9e9;
    --band-peach: #dcc3ae;
    --band-peach-light: #ead6c6;
    --band-teal: #b2dbda;
    --band-teal-light: #c6e7e5;
    --ink: #1c1c1c;
    --brand-ink: #4a4a4a;
  }
  * { margin: 0; padding: 0; box-sizing: border-box; }
  html, body {
    width: 1200px;
    height: 900px;
    overflow: hidden;
  }
  body {
    background: linear-gradient(180deg, #d2d2d2 0%, var(--canvas-bg) 45%, #ececec 100%);
    font-family: "Montserrat", sans-serif;
    color: var(--ink);
    position: relative;
  }
  .label {
    position: absolute;
    top: 427px;
    width: 200px;
    height: 278px;
    display: flex;
    flex-direction: column;
    background: linear-gradient(90deg, var(--label-sheen) 0%, var(--label-white) 30%, #fafafa 55%, var(--label-sheen) 100%);
  }
  .label--vitamin-c { left: 377px; }
  .label--hyaluronic { left: 617px; }
  .label__top {
    height: 181px;
    display: flex;
    flex-direction: column;
    align-items: center;
    text-align: center;
  }
  .brand-name {
    margin-top: 33px;
    font-weight: 300;
    font-size: 20px;
    letter-spacing: 0.5px;
    color: var(--brand-ink);
    text-transform: uppercase;
    white-space: nowrap;
  }
  .product-name {
    margin-top: 64px;
    text-transform: uppercase;
    font-weight: 500;
    line-height: 1.05;
  }
  .product-name__main { display: block; font-size: 21px; letter-spacing: 0.3px; }
  .product-name__sub { display: block; font-size: 14.5px; margin-top: 2px; }
  .label--hyaluronic .product-name { margin-top: 44px; }
  .label--hyaluronic .product-name__main,
  .label--hyaluronic .product-name__sub { font-size: 21px; margin-top: 0; }
  .label__band {
    flex: 1;
    display: flex;
    flex-direction: column;
    align-items: center;
    text-align: center;
  }
  .label--vitamin-c .label__band {
    background: linear-gradient(90deg, var(--band-peach) 0%, var(--band-peach-light) 40%, var(--band-peach) 100%);
  }
  .label--hyaluronic .label__band {
    background: linear-gradient(90deg, var(--band-teal) 0%, var(--band-teal-light) 40%, var(--band-teal) 100%);
  }
  .benefits {
    margin-top: 18px;
    font-size: 8.6px;
    line-height: 1.1;
    font-weight: 400;
  }
  .volume {
    margin-top: auto;
    margin-bottom: 11px;
    font-size: 8.2px;
    font-weight: 500;
    letter-spacing: 0.2px;
  }
</style>
</head>
<body>
  <section class="label label--vitamin-c">
    <div class="label__top">
      <p class="brand-name">Velora Fen</p>
      <h2 class="product-name">
        <span class="product-name__main">Vitamin C</span>
        <span class="product-name__sub">Brightening Serum</span>
      </h2>
    </div>
    <div class="label__band">
      <p class="benefits">Anti-Aging<br>Antioxidant</p>
      <p class="volume">50ML/1.7 FL. OZ.</p>
    </div>
  </section>

  <section class="label label--hyaluronic">
    <div class="label__top">
      <p class="brand-name">Velora Fen</p>
      <h2 class="product-name">
        <span class="product-name__main">Hyaluronic</span>
        <span class="product-name__sub">Acid Serum</span>
      </h2>
    </div>
    <div class="label__band">
      <p class="benefits">Deep Moisturizing<br>Improving Skin Elasticil</p>
      <p class="volume">50ML/1.7 FL. OZ.</p>
    </div>
  </section>
</body>
</html>
```